FinTech company looking to revamp and expand client-facing interface for our financial models

Halvern Ledgerworks currently has a very simple website that allows clients to interact with our financial models. We are looking to completely redesign the current site and add several extra pages to provide extra functionality. We want the design to have a modern, slick feel, that will work on both a desktop or a tablet. It should be straightforward for clients to move between different pages at any time, and clear from the layout how to interact with the more advanced features. We have included screenshots of existing pages in the attached design brief, as well as sketches of the functionality required by the new pages, but can't provide a direct link to the current site.
Target Market(s)
Professional investors that will be paying to access the interface
Industry/Entity Type
Finance
Number of Pages Required
4 page
Colors
Designer to choose colors to be used in the design.
Look and feel
Each slider illustrates characteristics of the customer's brand and the style your logo design should communicate.

```html
<!DOCTYPE html>
<html lang="en">
<head>
<meta charset="utf-8">
<title>Halvern Ledgerworks – Model Interface</title>
<link rel="stylesheet" href="https://fonts.googleapis.com/css2?family=Montserrat:wght@500;600;700&family=Roboto:wght@400;500;700&display=swap">
<style>
:root{
  --ink:#1b1f2a;
  --muted:#8a8a8a;
  --head-bg:#e4e4e4;
  --rule:#cfcfcf;
  --pos:#3fae3f;
  --neg:#e53935;
  --chart-bg:#222222;
  --grid:#3a3a3a;
  --area:#444444;
  --pink:#f0226e;
  --gold:#f5b800;
  --tip-up:#3c8a52;
  --tip-down:#c62834;
}
*{box-sizing:border-box;margin:0;padding:0}
html,body{width:1200px;height:497px;overflow:hidden;background:#fff}
.stage{position:absolute;top:0;left:0;width:2560px;height:1060px;transform:scale(0.46875);transform-origin:0 0;font-family:"Roboto",Arial,sans-serif;color:var(--ink)}
.abs{position:absolute}
.brand{left:8px;top:6px;font-size:8px;letter-spacing:.3px;font-family:"Roboto",sans-serif}
.horizons{display:flex;gap:22px;font-family:"Montserrat",sans-serif;font-weight:700;font-size:11px}
.horizons span{display:flex;align-items:center;gap:6px;color:#333}
.horizons span::before{content:"";width:7px;height:7px;border-radius:50%;background:var(--muted)}
.horizons .on::before{background:var(--ink)}
.horizons .on{color:var(--ink)}
.nav{display:flex;gap:48px;font-family:"Montserrat",sans-serif;font-weight:600;font-size:13px}
.nav a{color:var(--ink);text-decoration:none;padding-bottom:3px}
.nav a.active{border-bottom:2px solid var(--ink)}
.field{display:flex;align-items:center;font-size:10px}
.field b{font-weight:700}
.field .label{width:64px}
.field input{width:82px;height:12px;border:1px solid #bbb;border-radius:2px;font-size:6px;padding-left:6px;color:#666;font-family:inherit}
.filters{display:flex;gap:27px;font-size:8px;font-weight:500}
.filters span::after{content:"";display:inline-block;width:4px;height:4px;border-right:1.5px solid var(--ink);border-bottom:1.5px solid var(--ink);transform:rotate(45deg);margin-left:6px;position:relative;top:-2px}
.export{font-size:7px;display:flex;align-items:center;gap:5px}
.export i{width:7px;height:7px;border:1.2px solid var(--ink);display:inline-block}
table.data{position:absolute;border-collapse:collapse;table-layout:fixed;font-size:6px}
table.data th{background:var(--head-bg);height:28px;font-size:7px;font-weight:700;text-align:center}
table.data th.small{font-weight:400;font-size:6.5px}
table.data td{height:27px;border-bottom:1px solid var(--rule);text-align:center;line-height:1.2}
table.data td.name{font-weight:700;text-align:left;padding-left:12px}
table.data td.bold{font-weight:700}
table.data th.left{text-align:left;padding-left:6px}
.pos{color:var(--pos)}
.neg{color:var(--neg)}
.add{display:inline-block;width:6px;height:6px;border:1px solid #666;border-radius:50%;margin-right:10px;vertical-align:middle}
.title{font-size:10px;font-weight:700}
.pager{font-size:6px}
.axis{font-size:6px;font-weight:700;color:var(--ink)}
.chart{position:absolute}
</style>
</head>
<body>
<div class="stage">

  <!-- Models page -->
  <div class="abs brand">HALVERN</div>
  <div class="abs horizons" style="left:8px;top:18px"><span class="on">250D</span><span>83D</span><span>24D</span></div>
  <nav class="abs nav" style="left:437px;top:18px"><a class="active">models</a><a>sensitivities</a><a>favourites</a></nav>
  <div class="abs field" style="left:10px;top:76px"><span class="label"><b>Quality</b></span><input value="-10"></div>
  <div class="abs field" style="left:10px;top:90px"><span class="label"><b>Abs</b> (Stat)</span><input value="-10"></div>
  <div class="abs export" style="left:10px;top:123px"><i></i>Export</div>
  <div class="abs filters" style="left:74px;top:122px"><span>Filter 1</span><span>Filter 2</span></div>
  <table class="data" style="left:10px;top:143px;width:760px">
    <colgroup><col style="width:60px"><col style="width:67px"><col style="width:63px"><col style="width:63px"><col span="8" style="width:63px"></colgroup>
    <tr><th class="left">ID ▾</th><th>Sector</th><th>Time</th><th class="small">Quality</th><th class="small">Stat 1</th><th class="small">Stat 2</th><th class="small">Stat 3</th><th class="small">Stat 4</th><th class="small">Stat 5</th><th class="small">Stat 6</th><th class="small">Stat 7</th><th class="small">Stat 8</th></tr>
    <tr><td class="name" style="padding-left:8px"><span class="add"></span>Model 1</td><td>Materials</td><td><b>2019-07-03</b><br>12:50:00.000</td><td>30.1245</td><td class="pos">23.2253</td><td class="neg">-0.012536</td><td class="neg">-0.12795</td><td class="pos">12.0235</td><td class="pos">4.2356</td><td class="pos">0.69312</td><td class="pos">2.03023</td><td class="pos">2.3662</td></tr>
    <tr><td class="name" style="padding-left:8px"><span class="add"></span>Model 2</td><td>industrials</td><td><b>2019-07-03</b><br>12:50:00.000</td><td>1.2354</td><td class="neg">-0.03564</td><td class="pos">0.56230</td><td class="neg">-0.36265</td><td class="neg">-0.12486</td><td class="pos">81.26125</td><td class="neg">-0.023614</td><td class="neg">-0.12354</td><td class="pos">0.23517</td></tr>
    <tr><td class="name" style="padding-left:8px"><span class="add"></span>Model 3</td><td>Consumer<br>Discretionary</td><td><b>2019-07-03</b><br>12:50:00.000</td><td>72.2354</td><td class="pos">45.301</td><td class="pos">0.19785</td><td class="pos">0.36952</td><td class="pos">123.0289</td><td class="pos">3.69542</td><td class="neg">-0.21475</td><td class="neg">-0.01247</td><td class="pos">9.00235</td></tr>
    <tr><td class="name" style="padding-left:8px"><span class="add"></span>Model 4</td><td>Information<br>Technology</td><td><b>2019-07-03</b><br>12:50:00.000</td><td>36.2310</td><td class="pos">70.256</td><td class="neg">-0.12365</td><td class="pos">0.002354</td><td class="pos">51.30012</td><td class="pos">36.2615</td><td class="pos">0.1367</td><td class="neg">-0.69421</td><td class="pos">1.02358</td></tr>
    <tr><td class="name" style="padding-left:8px"><span class="add"></span>Model 5</td><td>Information<br>Technology</td><td><b>2019-07-03</b><br>12:50:00.000</td><td>45.2013</td><td class="pos">25.14395</td><td class="pos">0.39784</td><td class="neg">-0.51651</td><td class="pos">0.326452</td><td class="pos">11.00235</td><td class="pos">0.78941</td><td class="pos">1.87135</td><td class="pos">12.00473</td></tr>
  </table>

  <!-- Sensitivities page -->
  <div class="abs horizons" style="left:843px;top:18px"><span class="on">250D</span><span>83D</span><span>24D</span></div>
  <nav class="abs nav" style="left:1271px;top:18px"><a class="active">models</a><a>sensitivities</a><a>favourites</a></nav>
  <div class="abs field" style="left:845px;top:77px"><span class="label" style="width:86px"><b>Stat 1</b> Threshold</span><input value="-10"></div>
  <div class="abs field" style="left:845px;top:91px"><span class="label" style="width:86px"><b>Stat 1</b> Threshold</span><input value="-10"></div>
  <div class="abs field" style="left:845px;top:105px"><span class="label" style="width:86px"><b>Stat 1</b> Threshold</span><input value="-10"></div>
  <div class="abs filters" style="left:908px;top:123px"><span>Filter 1</span><span>Filter 2</span></div>
  <table class="data" style="left:845px;top:143px;width:760px">
    <colgroup><col style="width:105px"><col style="width:110px"><col style="width:165px"><col span="6" style="width:63px"></colgroup>
    <tr><th class="left" style="padding-left:12px">Factor</th><th>ID ▾</th><th>Sector</th><th class="small">Stat 1</th><th class="small">Stat 2</th><th class="small">Stat 3</th><th class="small">Stat 4</th><th class="small">Stat 5</th><th class="small">Stat 6</th></tr>
    <tr><td class="name">Factor</td><td class="bold">Model 1</td><td>Materials</td><td class="neg">- 1.4</td><td class="pos">0.1</td><td class="pos">3.7</td><td class="neg">- 3.07</td><td class="pos">30.3</td><td class="neg">- 0.36</td></tr>
    <tr><td class="name">Factor 1</td><td class="bold">Model 1</td><td>Materials</td><td class="pos">2.8</td><td class="pos">0.1</td><td class="pos">6.1</td><td class="neg">- 6.3</td><td class="pos">30.25</td><td class="neg">- 0.77</td></tr>
    <tr><td class="name">Factor 2</td><td class="bold">Model 1</td><td>Materials</td><td class="neg">- 3.7</td><td class="pos">2.7</td><td class="pos">7.2</td><td class="pos">2.3</td><td class="pos">30.69</td><td class="pos">0.47</td></tr>
    <tr><td class="name">Factor 3</td><td class="bold">Model 1</td><td>Industrials</td><td class="pos">2.8</td><td class="pos">0.2</td><td class="pos">2.7</td><td class="neg">- 3.01</td><td class="pos">31.96</td><td class="neg">- 0.60</td></tr>
    <tr><td class="name">Factor 4</td><td class="bold">Model 1</td><td>Industrials</td><td class="pos">0.8</td><td class="pos">0.3</td><td class="pos">2.5</td><td class="pos">1.89</td><td class="pos">32.6</td><td class="pos">0.5</td></tr>
  </table>
  <div class="abs pager" style="left:1586px;top:321px">25 <span style="font-size:8px">▾</span></div>

  <!-- Favourites page -->
  <div class="abs horizons" style="left:1678px;top:18px"><span class="on">250D</span><span>83D</span><span>24D</span></div>
  <nav class="abs nav" style="left:2105px;top:18px"><a class="active">models</a><a>sensitivities</a><a>favourites</a></nav>
  <div class="abs title" style="left:1679px;top:107px">Number of selected factors : 3</div>
  <div class="abs filters" style="left:1743px;top:123px"><span>Filter 1</span><span>Filter 2</span></div>
  <table class="data" style="left:1680px;top:143px;width:760px">
    <colgroup><col style="width:253px"><col span="4" style="width:126px"></colgroup>
    <tr><th class="left" style="padding-left:12px">ID ▾</th><th class="small">Stat 1</th><th class="small">Stat 2</th><th class="small">Stat 3</th><th class="small">Stat 4</th></tr>
    <tr><td class="name">Factor 1</td><td class="pos">0.0998</td><td class="pos">6.31</td><td class="pos">100</td><td class="pos">2.8</td></tr>
    <tr><td class="name">Factor 1</td><td class="pos">0.325</td><td class="neg">-12.6</td><td class="pos">0.7</td><td class="neg">-1.4</td></tr>
    <tr><td class="name">Factor 1</td><td class="pos">2.7</td><td class="neg">-1.08</td><td class="pos">100</td><td class="neg">-3.7</td></tr>
  </table>
  <div class="abs title" style="left:1680px;top:283px">Unselected Factors</div>
  <div class="abs filters" style="left:1743px;top:299px"><span>Filter 1</span><span>Filter 2</span></div>
  <table class="data" style="left:1680px;top:320px;width:760px">
    <colgroup><col span="6" style="width:126px"></colgroup>
    <tr><th class="small" style="font-weight:700">Factor</th><th class="small" style="font-weight:700">Factor</th><th class="small" style="font-weight:700">Factor</th><th class="small" style="font-weight:700">Factor</th><th class="small" style="font-weight:700">Factor</th><th class="small" style="font-weight:700">Factor</th></tr>
    <tr><td></td><td></td><td></td><td></td><td></td><td></td></tr>
    <tr><td></td><td></td><td></td><td></td><td></td><td></td></tr>
  </table>

  <!-- Area chart -->
  <div class="abs axis" style="left:1725px;top:468px">60</div>
  <div class="abs axis" style="left:1725px;top:500px">50</div>
  <div class="abs axis" style="left:1725px;top:530px">40</div>
  <div class="abs axis" style="left:1725px;top:563px">30</div>
  <div class="abs axis" style="left:1725px;top:593px">20</div>
  <svg class="chart" style="left:1743px;top:430px" width="696" height="183" viewBox="1743 430 696 183" aria-label="Factor performance area chart">
    <rect x="1743" y="430" width="696" height="183" rx="8" fill="var(--chart-bg)"/>
    <g stroke="var(--grid)" stroke-width="1">
      <line x1="1832" y1="430" x2="1832" y2="613"/><line x1="2005" y1="430" x2="2005" y2="613"/><line x1="2178" y1="430" x2="2178" y2="613"/><line x1="2351" y1="430" x2="2351" y2="613"/>
      <line x1="1743" y1="504" x2="2439" y2="504"/><line x1="1743" y1="534" x2="2439" y2="534"/><line x1="1743" y1="567" x2="2439" y2="567"/><line x1="1743" y1="597" x2="2439" y2="597"/>
    </g>
    <polygon fill="var(--area)" opacity=".8" points="1743,465 1770,488 1790,475 1812,490 1828,522 1855,532 1860,545 1865,545 1870,490 1885,520 1905,530 1928,533 1940,518 1945,525 1955,510 1960,525 1970,500 1975,515 1990,478 1993,512 2005,510 2020,520 2035,530 2055,550 2075,545 2095,537 2110,542 2135,515 2140,525 2155,535 2175,545 2195,560 2205,575 2225,560 2230,575 2260,568 2275,580 2285,575 2295,580 2320,560 2335,555 2345,585 2360,570 2370,575 2395,555 2439,508 2439,605 2431,613 1751,613 1743,605"/>
    <rect x="1798" y="464" width="29" height="16" rx="3" fill="var(--tip-up)"/>
    <polygon points="1809,480 1815,480 1812,484" fill="var(--tip-up)"/>
    <text x="1812" y="475" fill="#fff" font-size="7" font-weight="700" text-anchor="middle" font-family="Roboto,sans-serif">▴ 22%</text>
    <circle cx="1812" cy="491" r="1.8" fill="#5ccf7a"/>
    <rect x="2181" y="526" width="30" height="16" rx="3" fill="var(--tip-down)"/>
    <polygon points="2193,542 2199,542 2196,546" fill="var(--tip-down)"/>
    <text x="2196" y="537" fill="#fff" font-size="7" font-weight="700" text-anchor="middle" font-family="Roboto,sans-serif">▾ 16%</text>
    <circle cx="2196" cy="553" r="1.8" fill="#ff4a4a"/>
  </svg>

  <!-- Line chart -->
  <svg class="chart" style="left:1743px;top:672px" width="696" height="199" viewBox="1743 672 696 199" aria-label="Factor comparison line chart">
    <rect x="1743" y="672" width="696" height="199" fill="var(--chart-bg)"/>
    <g stroke="#333" stroke-width="1">
      <line x1="1785" y1="702" x2="2439" y2="702"/><line x1="1785" y1="745" x2="2439" y2="745"/><line x1="1785" y1="789" x2="2439" y2="789"/><line x1="1785" y1="832" x2="2439" y2="832"/>
      <line x1="1785" y1="672" x2="1785" y2="848"/><line x1="1829" y1="672" x2="1829" y2="848"/><line x1="1873" y1="672" x2="1873" y2="848"/><line x1="1917" y1="672" x2="1917" y2="848"/><line x1="1961" y1="672" x2="1961" y2="848"/><line x1="2005" y1="672" x2="2005" y2="848"/><line x1="2049" y1="672" x2="2049" y2="848"/><line x1="2093" y1="672" x2="2093" y2="848"/><line x1="2137" y1="672" x2="2137" y2="848"/><line x1="2181" y1="672" x2="2181" y2="848"/><line x1="2225" y1="672" x2="2225" y2="848"/><line x1="2269" y1="672" x2="2269" y2="848"/><line x1="2313" y1="672" x2="2313" y2="848"/><line x1="2357" y1="672" x2="2357" y2="848"/><line x1="2401" y1="672" x2="2401" y2="848"/>
    </g>
    <g fill="#fff" font-size="6.5" font-weight="700" font-family="Roboto,sans-serif">
      <text x="1760" y="705">25</text><text x="1760" y="748">20</text><text x="1760" y="792">15</text><text x="1760" y="835">0</text>
    </g>
    <g fill="#fff" font-size="6" font-weight="700" font-family="Roboto,sans-serif" text-anchor="middle">
      <text x="1807" y="862">Jun 1</text><text x="1851" y="862">Jun 2</text><text x="1894" y="862">Jun 3</text><text x="1938" y="862">Jun 4</text><text x="1982" y="862">Jun 5</text><text x="2027" y="862">Jun 6</text><text x="2070" y="862">Jun 7</text><text x="2114" y="862">Jun 8</text><text x="2158" y="862">Jun 9</text><text x="2202" y="862">Jun 10</text><text x="2245" y="862">Jun 11</text><text x="2289" y="862">Jun 12</text><text x="2333" y="862">Jun 13</text><text x="2378" y="862">Jun 14</text><text x="2421" y="862">Jun 1</text>
    </g>
    <polyline fill="none" stroke="var(--gold)" stroke-width="1.5" points="1803,815 1843,813 1883,773 1923,786 1963,820 2003,802 2043,818 2083,821 2123,814 2163,800 2203,806 2243,760 2283,793 2323,816 2363,800 2403,818 2439,757"/>
    <polyline fill="none" stroke="var(--pink)" stroke-width="1.5" points="1797,797 1837,778 1877,795 1917,771 1957,738 1997,784 2037,778 2077,792 2117,799 2157,797 2197,780 2237,798 2277,763 2317,751 2357,791 2397,793"/>
    <g fill="var(--gold)">
      <circle cx="1803" cy="815" r="3"/><circle cx="1843" cy="813" r="3"/><circle cx="1883" cy="773" r="3"/><circle cx="1923" cy="786" r="3"/><circle cx="1963" cy="820" r="3"/><circle cx="2003" cy="802" r="3"/><circle cx="2043" cy="818" r="3"/><circle cx="2083" cy="821" r="3"/><circle cx="2123" cy="814" r="3"/><circle cx="2163" cy="800" r="3"/><circle cx="2203" cy="806" r="3"/><circle cx="2243" cy="760" r="3"/><circle cx="2283" cy="793" r="3"/><circle cx="2323" cy="816" r="3"/><circle cx="2363" cy="800" r="3"/><circle cx="2403" cy="818" r="3"/>
    </g>
    <g fill="var(--pink)">
      <circle cx="1797" cy="797" r="3"/><circle cx="1837" cy="778" r="3"/><circle cx="1877" cy="795" r="3"/><circle cx="1917" cy="771" r="3"/><circle cx="1957" cy="738" r="3"/><circle cx="1997" cy="784" r="3"/><circle cx="2037" cy="778" r="3"/><circle cx="2077" cy="792" r="3"/><circle cx="2117" cy="799" r="3"/><circle cx="2157" cy="797" r="3"/><circle cx="2197" cy="780" r="3"/><circle cx="2237" cy="798" r="3"/><circle cx="2277" cy="763" r="3"/><circle cx="2317" cy="751" r="3"/><circle cx="2357" cy="791" r="3"/><circle cx="2397" cy="793" r="3"/>
    </g>
  </svg>

</div>
</body>
</html>
```